Top of the line business card design needed for real estate brokerage

We currently have a business card with our logo but would like to have a revised version. We would love for you to implement your own design that will catch anyone's attention. The theme colors should be black, royal blue, gray/silver, and white.The contact information should be the same as the info on our current business card (picture attached). In the design that we pick, we will need to be able to edit the text so that we can customize the text content for each of our agents. Same goes for the professional picture. There should be an area on the card that each agent can have their professional portrait attached. Please include a version without the picture option as well for agents that do not wish to have a professional picture attached.

```html
<!DOCTYPE html>
<html lang="en">
<head>
<meta charset="utf-8">
<title>Clearstone Realty – Business Card</title>
<link href="https://fonts.googleapis.com/css2?family=Lato:wght@400;700&display=swap" rel="stylesheet">
<style>
  :root {
    --royal-blue: #0a6cc4;
    --deep-blue: #0556a3;
    --ink: #1d1d1f;
    --silver: #c9ccd0;
    --paper: #f7f7f7;
    --backdrop: #e4e2de;
    --white: #ffffff;
  }
  * { box-sizing: border-box; margin: 0; padding: 0; }
  html, body {
    width: 1200px; height: 780px; overflow: hidden;
    background: var(--backdrop);
    font-family: "Lato", Arial, sans-serif;
  }
  .sheet {
    position: relative; width: 1200px; height: 780px;
    display: flex; align-items: center; justify-content: center; gap: 40px;
  }
  .card {
    position: relative; width: 540px; height: 309px;
    background: var(--paper);
    box-shadow: 0 6px 18px rgba(0,0,0,.18);
    overflow: hidden;
  }
  /* front */
  .card-front__wave { position: absolute; inset: 0; }
  .brand {
    position: absolute; display: flex; align-items: center; gap: 10px;
    white-space: nowrap;
  }
  .brand__mark { width: 22px; height: 22px; background: var(--royal-blue); flex: none; }
  .brand__name {
    font-weight: 700; font-size: 26px; color: var(--ink); letter-spacing: .5px;
  }
  .card-front .brand { left: 26px; top: 196px; gap: 8px; }
  .card-front .brand__mark { width: 18px; height: 18px; }
  .card-front .brand__name { font-size: 21px; letter-spacing: .3px; }
  .agent {
    position: absolute; left: 340px; top: 34px; color: var(--white);
  }
  .agent__name { font-weight: 700; font-size: 22px; }
  .agent__title { font-size: 13px; margin-top: 2px; }
  .contacts {
    position: absolute; left: 318px; top: 128px; list-style: none;
    color: var(--white); font-size: 14.5px;
  }
  .contacts li { display: flex; align-items: center; gap: 8px; height: 27px; white-space: nowrap; }
  .contacts svg { width: 16px; height: 16px; flex: none; }
  /* back */
  .skyline {
    position: absolute; left: 0; top: 0; width: 540px; height: 252px;
    background: linear-gradient(180deg, #f4f4f4 0%, #e4e5e7 55%, #f1f1f1 100%);
  }
  .card-back .brand { left: 150px; top: 108px; }
  .card-back .brand__name { font-size: 30px; }
  .services {
    position: absolute; left: 0; bottom: 0; width: 100%; height: 57px;
    background: var(--royal-blue); color: var(--white);
    font-size: 14px; padding: 9px 0 0 34px; line-height: 20px;
  }
  .services__extra { padding-left: 60px; }
</style>
</head>
<body>
<main class="sheet">

  <section class="card card-front" aria-label="Card front">
    <svg class="card-front__wave" viewBox="0 0 540 309" aria-hidden="true">
      <path d="M296 0 C 326 120 236 190 262 309 L540 309 L540 0 Z" fill="#1d1d1f"/>
      <path d="M304 0 C 336 120 248 190 274 309 L540 309 L540 0 Z" fill="var(--royal-blue)"/>
    </svg>

    <div class="brand">
      <span class="brand__mark"></span>
      <span class="brand__name">Clearstone Realty</span>
    </div>

    <div class="agent">
      <div class="agent__name">Marcus Hale</div>
      <div class="agent__title">Broker</div>
    </div>

    <ul class="contacts">
      <li><svg viewBox="0 0 16 16"><rect x="0" y="0" width="16" height="16" fill="#fff"/><rect x="3" y="4" width="10" height="7" fill="var(--royal-blue)"/></svg>555-210-4871</li>
      <li><svg viewBox="0 0 16 16"><rect width="16" height="16" fill="#fff"/><path d="M4 3h3l1 3-2 1a7 7 0 0 0 3 3l1-2 3 1v3h-2A9 9 0 0 1 4 5z" fill="var(--royal-blue)"/></svg>555-210-4872</li>
      <li><svg viewBox="0 0 16 16"><rect width="16" height="16" fill="#fff"/><rect x="5" y="2" width="6" height="12" rx="1" fill="var(--royal-blue)"/></svg>555-318-6640</li>
      <li><svg viewBox="0 0 16 16"><rect width="16" height="16" fill="#fff"/><rect x="2" y="4" width="12" height="8" fill="var(--royal-blue)"/><path d="M2 4l6 5 6-5" stroke="#fff" fill="none"/></svg>marcus@clearstonerealty.com</li>
      <li><svg viewBox="0 0 16 16"><rect width="16" height="16" fill="#fff"/><circle cx="8" cy="8" r="5.5" fill="none" stroke="var(--royal-blue)" stroke-width="1.4"/><path d="M2.5 8h11M8 2.5v11" stroke="var(--royal-blue)" stroke-width="1.2"/></svg>www.clearstonerealty.com</li>
    </ul>
  </section>

  <section class="card card-back" aria-label="Card back">
    <div class="skyline" role="img" aria-label="Faint grey line drawing of a city skyline"></div>
    <div class="brand">
      <span class="brand__mark"></span>
      <span class="brand__name">Clearstone Realty</span>
    </div>
    <div class="services">
      <div>Residential Real Estate | Commercial Estate | Property Management</div>
      <div class="services__extra">Investments</div>
    </div>
  </section>

</main>
</body>
</html>
```